Business cards Dör Kornhüüs GmbH & Co.KG

We need a uniform business card design template for our employees.
A template should be created to have the same design for all business cards.

Contact Information for Business Card

Firma und Firmierung, Name, Funktion in Unternehmen, Anschrift, Tel. Handynummer, Emailadresse, Internetseite

Colors

Designer to choose colors to be used in the design.

Requirements
Must have
• Our company logo must be on it

```html
<!DOCTYPE html>
<html lang="de">
<head>
<meta charset="utf-8">
<title>Dör Kornhüüs – Visitenkarten</title>
<link rel="stylesheet" href="https://fonts.googleapis.com/css2?family=Lato:wght@400;700;900&display=swap">
<style>
  :root {
    --stage: #2b2d31;
    --card: #151315;
    --lavender: #c697cf;
    --lavender-text: #b68cc2;
    --rose: #e36a80;
    --white: #f4f0f4;
    --divider: #8c6f93;
  }
  * { box-sizing: border-box; margin: 0; padding: 0; }
  html, body { width: 1200px; height: 900px; overflow: hidden; }
  body {
    background: var(--stage);
    font-family: "Lato", Arial, sans-serif;
    display: flex;
    align-items: center;
    justify-content: center;
    gap: 36px;
  }
  .card {
    position: relative;
    width: 560px;
    height: 320px;
    background: var(--card);
    border-radius: 4px;
    overflow: hidden;
  }
  .brand {
    display: flex;
    align-items: center;
    gap: 10px;
  }
  .brand-dot {
    width: 14px; height: 14px;
    border-radius: 50%;
    background: var(--rose);
    flex: none;
  }
  .brand-name {
    font-weight: 900;
    color: var(--rose);
    letter-spacing: 1px;
    text-transform: uppercase;
  }
  .brand-tagline {
    color: var(--lavender-text);
    letter-spacing: 3px;
    font-size: 13px;
    margin-top: 4px;
  }

  /* contact side */
  .card--contact .brand-block {
    position: absolute;
    left: 40px; top: 92px;
    width: 210px;
  }
  .card--contact .brand-name { font-size: 26px; }
  .card--contact .divider {
    position: absolute;
    left: 262px; top: 78px;
    width: 1px; height: 118px;
    background: var(--divider);
  }
  .person {
    position: absolute;
    left: 284px; top: 80px;
  }
  .person-name {
    color: var(--rose);
    font-weight: 900;
    font-size: 21px;
    letter-spacing: 1.5px;
    text-transform: uppercase;
  }
  .person-role {
    color: var(--lavender-text);
    font-size: 15px;
    margin: 2px 0 10px;
  }
  .contact-list { list-style: none; }
  .contact-list li {
    display: flex;
    align-items: center;
    gap: 8px;
    color: var(--lavender-text);
    font-size: 15px;
    line-height: 22px;
  }
  .contact-list svg { width: 13px; height: 13px; flex: none; }
  .address-band {
    position: absolute;
    left: 0; right: 0; bottom: 0;
    height: 40px;
    background: var(--lavender);
    color: #3a2a3e;
    font-size: 15px;
    display: flex;
    align-items: center;
    padding-left: 40px;
    letter-spacing: .5px;
  }

  /* brand side */
  .card--brand .brand-block {
    position: absolute;
    left: 0; right: 0; top: 100px;
    display: flex;
    flex-direction: column;
    align-items: center;
  }
  .card--brand .brand-name { font-size: 36px; }
  .card--brand .brand-tagline { font-size: 15px; letter-spacing: 5px; }
  .services {
    position: absolute;
    left: 0; right: 0; bottom: 40px;
    text-align: center;
    color: var(--white);
    font-size: 12.5px;
    letter-spacing: .3px;
    text-transform: uppercase;
  }
  .services .bullet { color: var(--rose); margin: 0 4px; }
</style>
</head>
<body>

  <section class="card card--contact">
    <div class="brand-block">
      <div class="brand">
        <span class="brand-dot"></span>
        <span class="brand-name">Dör Kornhüüs</span>
      </div>
      <p class="brand-tagline">Nordische Backkunst</p>
    </div>
    <div class="divider"></div>
    <div class="person">
      <h1 class="person-name">Jonas Weber</h1>
      <p class="person-role">Sales Manager</p>
      <ul class="contact-list">
        <li>
          <svg viewBox="0 0 16 16" aria-hidden="true"><circle cx="8" cy="8" r="7" fill="none" stroke="#e36a80" stroke-width="1.6"/><path d="M5.5 4.5l1.5 1.5-1 1c.6 1.3 1.7 2.4 3 3l1-1 1.5 1.5-1 1c-2.8-.4-5-2.6-5.4-5.4z" fill="#e36a80"/></svg>
          604-555-0192
        </li>
        <li>
          <svg viewBox="0 0 16 16" aria-hidden="true"><rect x="1.5" y="3.5" width="13" height="9" fill="none" stroke="#e36a80" stroke-width="1.6"/><path d="M1.5 3.5l6.5 5 6.5-5" fill="none" stroke="#e36a80" stroke-width="1.4"/></svg>
          info@doerkornhuues.com
        </li>
        <li>
          <svg viewBox="0 0 16 16" aria-hidden="true"><circle cx="8" cy="8" r="7" fill="#e36a80"/><path d="M1 8h14M8 1c3 3 3 11 0 14M8 1c-3 3-3 11 0 14" fill="none" stroke="#151315" stroke-width="1"/></svg>
          www.doerkornhuues.com
        </li>
      </ul>
    </div>
    <div class="address-band">PO Box 318, Ravensdale Qld 4870</div>
  </section>

  <section class="card card--brand">
    <div class="brand-block">
      <div class="brand">
        <span class="brand-dot"></span>
        <span class="brand-name">Dör Kornhüüs</span>
      </div>
      <p class="brand-tagline">Nordische Backkunst</p>
    </div>
    <p class="services">
      <span class="bullet">●</span>Lack of Confidence
      <span class="bullet">●</span>Conflicting Emotions
      <span class="bullet">●</span>No Energy
      <span class="bullet">●</span>Phobias
    </p>
  </section>

</body>
</html>
```